One page website

I'm looking for a landing page for my company. Just a brief description of our medical device technology with some images

Coding

Coded - Design and coding required

```html
<!DOCTYPE html>
<html lang="en">
<head>
<meta charset="utf-8">
<title>Kinora Medical — Solving Children's Scoliosis</title>
<link href="https://fonts.googleapis.com/css2?family=Roboto:wght@400;500;700&display=swap" rel="stylesheet">
<style>
:root{
  --green:#7cc142;
  --green-dark:#5ea82c;
  --blue:#3d8fd6;
  --ink:#1f1f1f;
  --text:#444;
  --muted:#777;
  --footer-bar:#55b3de;
}
*{margin:0;padding:0;box-sizing:border-box}
html,body{width:1200px;height:4762px;overflow:hidden}
body{position:relative;background:#fff;font-family:'Roboto',sans-serif;color:var(--ink)}
.abs{position:absolute}
.brand{font-family:'Roboto',sans-serif;font-weight:500;color:var(--green);display:flex;align-items:center;gap:8px;white-space:nowrap}
.brand .dot{width:12px;height:12px;border-radius:50%;background:var(--blue);flex-shrink:0}
/* header */
.site-header{position:absolute;left:0;top:0;width:1200px;height:137px;background:#fff}
.site-header .brand{position:absolute;left:118px;top:60px;font-size:23px}
.main-nav{position:absolute;left:337px;top:66px;display:flex;gap:31px;font-size:13px;color:#333}
.main-nav a{color:#333;text-decoration:none;position:relative}
.main-nav a.active{font-weight:700;color:#111}
.main-nav a.active::after{content:"";position:absolute;left:-4px;right:-4px;top:42px;height:4px;background:var(--blue)}
.social{position:absolute;left:988px;top:66px;display:flex;gap:30px}
.social span{width:14px;height:14px;border-radius:50%;background:#222}
/* hero */
.hero{position:absolute;left:0;top:137px;width:1200px;height:690px;background:linear-gradient(180deg,#ececee,#dcdcde)}
.hero-photo{position:absolute;left:440px;top:0;width:760px;height:690px;background:radial-gradient(ellipse at 60% 45%,#f1efee 0%,#d4d2d3 55%,#b9b9bc 100%)}
.hero-dots{position:absolute;left:97px;top:243px;display:flex;flex-direction:column;gap:16px}
.hero-dots span{width:12px;height:12px;border-radius:50%;background:#111}
.hero-dots span.on{background:#fff}
.hero-title{position:absolute;left:175px;top:215px;font-size:40px;font-weight:700;line-height:50px;color:#111}
.bar{display:block;width:52px;height:4px;background:var(--blue)}
.bar.g{background:var(--green)}
.hero .bar{position:absolute;left:177px;top:207px}
.hero .bar.g{top:377px}
.hero-note{position:absolute;left:181px;top:388px;font-size:11px;color:#333}
.hero-wave{position:absolute;left:0;top:520px}
/* section heads */
.sec-head{position:absolute;left:0;width:1200px;text-align:center}
.sec-head .bar{margin:0 auto 18px}
.sec-head h2{font-size:29px;font-weight:700;color:#111}
.sec-head p{font-size:19px;color:#333;margin-top:14px}
.sec-head .eyebrow{font-size:13px;color:var(--green-dark);font-weight:500;margin-bottom:12px}
/* mission */
.mission .bar{position:absolute;left:167px;top:910px}
.mission h2{position:absolute;left:167px;top:925px;font-size:29px;font-weight:700}
.mission p{position:absolute;left:167px;top:980px;width:420px;font-size:16px;line-height:26px;color:#222}
.btn{position:absolute;left:164px;top:1086px;width:185px;height:60px;border-radius:30px;background:linear-gradient(90deg,var(--green-dark),var(--green));color:#fff;font-size:18px;font-weight:700;display:flex;align-items:center;justify-content:center}
.mission-img{position:absolute;left:644px;top:890px;width:446px;height:293px;background:linear-gradient(90deg,#f4f5f6 0%,#e9eaec 45%,#c9c3c8 80%,#a9a7c8 100%)}
/* benefits */
.bg-swirl{position:absolute;left:0;width:1200px;background:radial-gradient(ellipse at 20% 50%,#eeeeef 0%,rgba(255,255,255,0) 60%),radial-gradient(ellipse at 85% 40%,#f0f0f1 0%,rgba(255,255,255,0) 55%)}
.benefit{position:absolute;display:flex;align-items:center;gap:22px;font-size:19px;line-height:25px;color:#222}
.benefit.left{text-align:right}
.icon-ring{width:92px;height:92px;border-radius:50%;border:5px dotted #bbb;display:flex;align-items:center;justify-content:center;flex-shrink:0;background:#fff}
.icon-ring svg{width:44px;height:44px}
/* solutions */
.sol-list{position:absolute;left:155px;top:2135px}
.sol-item{position:absolute;left:0;display:flex;align-items:center;gap:32px;width:400px;font-size:19px;line-height:26px;color:#666}
.sol-item .tick{width:74px;height:74px;border-radius:50%;background:linear-gradient(135deg,var(--green) 0%,var(--green-dark) 50%,#2f7d8f 100%);display:flex;align-items:center;justify-content:center;flex-shrink:0}
.sol-item b{color:#111}
.sol-img{position:absolute;left:579px;top:2134px;width:511px;height:394px;background:linear-gradient(90deg,#6b5f4f,#3f4656 40%,#2a2f3c)}
.sol-img .panel{position:absolute;left:0;top:0;width:167px;height:394px;background:var(--green)}
.sol-img .panel h4{position:absolute;left:0;top:52px;width:167px;text-align:center;color:#fff;font-size:16px;font-weight:500;line-height:26px}
.sol-img .device{position:absolute;left:18px;top:124px;width:127px;height:206px;background:linear-gradient(135deg,#2d3c52,#8a98ad);border:2px solid #111}
.sol-img .spine{position:absolute;left:167px;top:0;width:344px;height:394px;background:radial-gradient(ellipse at 70% 50%,#c8a979 0%,#8b7150 30%,#3b4250 70%)}
.sol-img .lbl{position:absolute;left:185px;font-size:11px;line-height:13px;color:#fff;width:100px}
/* team */
.member{position:absolute;width:240px;text-align:center}
.avatar{width:164px;height:164px;margin:0 auto;border-radius:50%;padding:8px;background:linear-gradient(135deg,var(--green),var(--blue))}
.avatar div{width:100%;height:100%;border-radius:50%;border:5px solid #fff;background:linear-gradient(160deg,#9aa1a9,#4b4f56)}
.member h3{font-size:16px;font-weight:700;margin-top:26px;color:#111}
.member .role{font-size:11px;color:#333;margin-top:6px;line-height:15px}
.member .bio{font-size:10.5px;color:#333;margin-top:22px;line-height:20px}
/* how */
.how{position:absolute;left:0;top:3704px;width:1200px;height:619px;background:radial-gradient(ellipse at 55% 40%,#8a5a43 0%,#5a3a2d 35%,#2b2227 70%,#1d1c22 100%)}
.how h2{position:absolute;left:0;top:212px;width:1200px;text-align:center;color:#fff;font-size:29px;font-weight:700}
.play{position:absolute;left:564px;top:262px;width:72px;height:72px;border-radius:50%;background:#222;display:flex;align-items:center;justify-content:center}
.how .brand{position:absolute;left:0;top:430px;width:1200px;justify-content:center;font-size:30px}
.player{position:absolute;left:280px;top:551px;width:640px;height:30px;background:#fff;border-radius:3px;display:flex;align-items:center;padding:0 8px;gap:8px;font-size:9px;color:#555}
.player .pbtn{width:20px;height:20px;border-radius:50%;background:#f07c2b}
.player .track{flex:1;height:3px;background:#ccc;margin:0 10px}
.player .sm{width:10px;height:10px;border-radius:50%;background:#f07c2b}
.player .gr{width:10px;height:10px;border-radius:50%;background:#999}
/* footer */
.site-footer .brand{position:absolute;left:116px;top:4410px;font-size:28px}
.foot-about{position:absolute;left:116px;top:4495px;width:210px;font-size:13px;line-height:21px;color:#666}
.contact{position:absolute;left:116px;font-size:13px;font-weight:500;color:#222;display:flex;align-items:center;gap:14px}
.contact svg{width:14px;height:14px}
.foot-col{position:absolute;top:4398px}
.foot-col .bar{width:52px;height:4px}
.foot-col h4{font-size:19px;font-weight:500;color:#333;margin-top:18px}
.foot-col ul{list-style:none;margin-top:22px}
.foot-col li{font-size:13px;font-weight:500;color:#222;height:31px;display:flex;gap:14px;align-items:flex-start}
.foot-col li::before{content:"";width:6px;height:6px;border-right:1.5px solid #888;border-top:1.5px solid #888;transform:rotate(45deg);margin-top:4px}
.foot-col li.closed{color:var(--blue)}
.copy{position:absolute;left:0;top:4715px;width:1200px;height:47px;background:var(--footer-bar);color:#fff;font-size:11px;text-align:center;line-height:47px}
</style>
</head>
<body>

<header class="site-header">
  <div class="brand"><span class="dot"></span>Kinora Medical</div>
  <nav class="main-nav">
    <a class="active">HOME</a><a>ABOUT US</a><a>SOLUTIONS</a><a>HOW IT WORKS</a><a>TESTIMONIALS</a><a>CONTACT US</a>
  </nav>
  <div class="social"><span></span><span></span><span></span></div>
</header>

<section class="hero">
  <div class="hero-photo" role="img" aria-label="Smiling girl balancing on a grey exercise ball with arms stretched out while a therapist holds her feet"></div>
  <div class="hero-dots"><span></span><span></span><span class="on"></span><span></span></div>
  <span class="bar"></span>
  <h1 class="hero-title">SOLVING<br>CHILDREN’S<br>SCOLIOSIS</h1>
  <span class="bar g"></span>
  <p class="hero-note">not approved for sale in the US</p>
  <svg class="hero-wave" width="1200" height="170" viewBox="0 0 1200 170">
    <path d="M0 60 C250 0 500 40 750 120 C900 165 1080 160 1200 130 L1200 170 L0 170 Z" fill="#fff"/>
    <path d="M0 60 C250 0 500 40 750 120 C900 165 1080 160 1200 130" fill="none" stroke="var(--green)" stroke-width="6"/>
  </svg>
</section>

<section class="mission">
  <span class="bar abs"></span>
  <h2>MISSION</h2>
  <p>Develop novel technologies focusing on non-fusion scoliosis correction allowing for non-surgical dynamic adjustment of implants over time.</p>
  <div class="btn">Read more</div>
  <div class="mission-img" role="img" aria-label="Girl stretching a blue exercise band with her smiling grandmother behind her, beside a green medical cross emblem"></div>
</section>

<div class="bg-swirl" style="top:1240px;height:680px"></div>
<section class="benefits">
  <div class="sec-head" style="top:1270px">
    <span class="bar"></span>
    <p class="eyebrow">ADVANTAGES OF VBT OVER FUSION</p>
    <h2>BENEFITS</h2>
  </div>
  <div class="benefit left" style="left:262px;top:1425px">
    <span>Continued<br>skeletal growth</span>
    <div class="icon-ring"><svg viewBox="0 0 44 44"><path d="M8 36V26h6v10M18 36V20h6v16M28 36V14h6v22M6 36h32M26 12l8-6 4 6" fill="none" stroke="var(--green-dark)" stroke-width="2"/></svg></div>
  </div>
  <div class="benefit" style="left:645px;top:1457px">
    <div class="icon-ring"><svg viewBox="0 0 44 44"><circle cx="22" cy="15" r="8" fill="none" stroke="var(--green-dark)" stroke-width="2"/><path d="M8 38c2-9 8-13 14-13s12 4 14 13" fill="none" stroke="var(--blue)" stroke-width="2"/></svg></div>
    <span>Little impact on activity<br>and appearance</span>
  </div>
  <div class="benefit left" style="left:192px;top:1605px">
    <span>Partial Motion<br>Preservation</span>
    <div class="icon-ring"><svg viewBox="0 0 44 44"><circle cx="22" cy="18" r="12" fill="none" stroke="var(--green-dark)" stroke-width="2"/><path d="M22 30v10M22 12v10l4 3" fill="none" stroke="var(--blue)" stroke-width="2"/></svg></div>
  </div>
  <div class="benefit" style="left:694px;top:1605px">
    <div class="icon-ring"><svg viewBox="0 0 44 44"><path d="M14 34V12l-6 6M14 12l6 6M30 10v22l-6-6M30 32l6-6" fill="none" stroke="var(--blue)" stroke-width="2"/></svg></div>
    <span>Does not <b>“burn any bridge”</b>:<br>fusion remains an unimpacted<br>option if this treatment<br>modality fails</span>
  </div>
  <div class="benefit left" style="left:362px;top:1752px">
    <span>Single treatment<br>event</span>
    <div class="icon-ring"><svg viewBox="0 0 44 44"><rect x="6" y="12" width="32" height="24" rx="3" fill="none" stroke="var(--green-dark)" stroke-width="2"/><path d="M17 12V8h10v4M22 18v12M16 24h12" fill="none" stroke="var(--blue)" stroke-width="2"/></svg></div>
  </div>
</section>

<section class="solutions">
  <div class="sec-head" style="top:1973px">
    <span class="bar"></span>
    <h2>OUR SOLUTIONS</h2>
    <p>Kinora Dynamic Tethering System</p>
  </div>
  <div class="sol-list">
    <div class="sol-item" style="top:0"><span class="tick"><svg width="24" height="18" viewBox="0 0 24 18"><path d="M3 9l6 6L21 3" fill="none" stroke="#fff" stroke-width="3"/></svg></span><span>Dynamic tension</span></div>
    <div class="sol-item" style="top:95px"><span class="tick"><svg width="24" height="18" viewBox="0 0 24 18"><path d="M3 9l6 6L21 3" fill="none" stroke="#fff" stroke-width="3"/></svg></span><span>Complete non-surgical<br>adjustment</span></div>
    <div class="sol-item" style="top:190px"><span class="tick"><svg width="24" height="18" viewBox="0 0 24 18"><path d="M3 9l6 6L21 3" fill="none" stroke="#fff" stroke-width="3"/></svg></span><span>Most effective in making<br>gradual non-surgical<br>adjustments over time</span></div>
    <div class="sol-item" style="top:285px"><span class="tick"><svg width="24" height="18" viewBox="0 0 24 18"><path d="M3 9l6 6L21 3" fill="none" stroke="#fff" stroke-width="3"/></svg></span><span>Prevents over-correction and<br>can act as <b>internal brace</b></span></div>
  </div>
  <div class="sol-img">
    <div class="panel"><h4>External<br>controller</h4>
      <div class="device" role="img" aria-label="Hand holding the handheld external controller"></div></div>
    <div class="spine" role="img" aria-label="Rendered spine with the tethering implant attached along the vertebrae"></div>
    <p class="lbl" style="top:30px">Anchoring<br>screw with<br>cleat mechanism</p>
    <p class="lbl" style="top:172px">Slider screws</p>
    <p class="lbl" style="top:245px">Adjustment<br>engine attached<br>to vertebral body<br>via screw. Tether<br>wraps around<br>spool. Spool<br>powered via<br>external<br>controller</p>
  </div>
</section>

<div class="bg-swirl" style="top:2760px;height:700px"></div>
<section class="team">
  <div class="sec-head" style="top:2645px">
    <span class="bar"></span>
    <h2>OUR TEAM</h2>
    <p>Founding Team – Experience in Orthopedic Implants</p>
  </div>
  <div class="member" style="left:104px;top:2817px">
    <div class="avatar"><div role="img" aria-label="Portrait of Alan Whitfield"></div></div>
    <h3>Alan Whitfield</h3><p class="role">Founder and CEO</p>
    <p class="bio">Co-founder and CEO of Meridian Ortho<br>Innovations- Acquired by Axisline in<br>2014 Leadership positions at Northbay<br>Labs and Calder</p>
  </div>
  <div class="member" style="left:354px;top:2817px">
    <div class="avatar"><div role="img" aria-label="Portrait of Ravi Menon"></div></div>
    <h3>Ravi Menon Ph.D.</h3><p class="role">Co-Founder Chief Science Officer</p>
    <p class="bio">Previous Chief Science Officer at<br>Meridian Ortho. Previous<br>leadership positions at Spanwell,<br>Axisline and Orthovance</p>
  </div>
  <div class="member" style="left:604px;top:2817px">
    <div class="avatar"><div role="img" aria-label="Portrait of Peter Hollis"></div></div>
    <h3 style="margin-top:20px">Peter Hollis</h3><p class="role">Co-Founder VP of R&amp;D and Operations</p>
    <p class="bio">Previous VP of R&amp;D at Meridian Ortho<br>Innovations<br>Previous leadership positions at<br>Coreflex, Lumora, Tessel<br>and Brightmoor Devices</p>
  </div>
  <div class="member" style="left:854px;top:2817px">
    <div class="avatar"><div role="img" aria-label="Portrait of Owen Marsh"></div></div>
    <h3 style="margin-top:16px">Owen Marsh</h3><p class="role">Co-founder and Senior R&amp;D Engineer</p>
    <p class="bio">Senior R&amp;D engineer at Westbrook<br>University,<br>Oakland</p>
  </div>
  <div class="member" style="left:229px;top:3243px">
    <div class="avatar"><div role="img" aria-label="Portrait of Samir Haddad"></div></div>
    <h3 style="margin-top:20px">Samir Haddad, MD</h3><p class="role">Professor and Chief of Pediatric<br>Orthopedics, Bayview Medical School</p>
    <p class="bio">60+ tethering procedures performed</p>
  </div>
  <div class="member" style="left:479px;top:3243px">
    <div class="avatar"><div role="img" aria-label="Portrait of Daniel Cho"></div></div>
    <h3 style="margin-top:20px">Daniel Cho, MD</h3><p class="role">Neurosurgeon at Harbor Children's<br>Hospital, Easton</p>
    <p class="bio">60+ tethering procedures performed</p>
  </div>
  <div class="member" style="left:729px;top:3243px">
    <div class="avatar"><div role="img" aria-label="Portrait of Arjun Sethi"></div></div>
    <h3 style="margin-top:18px">Arjun Sethi, MD</h3><p class="role" style="line-height:21px">Professor of Surgery and Pediatrics<br>at Lakeside Children's Hospital<br>and attending surgeon at<br>Harbor Children's Hospital,<br>Easton</p>
    <p class="bio" style="margin-top:12px">300+ tethering procedures performed</p>
  </div>
</section>

<section class="how" role="img" aria-label="Video background showing a child's back and spine">
  <h2>HOW IT WORKS</h2>
  <div class="play"><svg width="24" height="28" viewBox="0 0 24 28"><path d="M4 2l18 12L4 26z" fill="#fff"/></svg></div>
  <div class="brand"><span class="dot"></span>Kinora Medical</div>
  <div class="player"><span class="pbtn"></span><span class="track"></span><span class="sm"></span><span class="sm"></span><span>00:00:00</span><span class="gr"></span><span class="gr"></span></div>
</section>

<footer class="site-footer">
  <div class="brand"><span class="dot"></span>Kinora Medical</div>
  <p class="foot-about">We are ipsum dolor sit amet aeeatt consectetuer adipiscing elitseder diam nonummy.</p>
  <p class="contact" style="top:4578px"><svg viewBox="0 0 14 14"><path d="M7 13S2 8 2 5a5 5 0 0 1 10 0c0 3-5 8-5 8z" fill="none" stroke="#555" stroke-width="1.3"/><circle cx="7" cy="5" r="1.6" fill="#555"/></svg>14 Elm Row, 3300 Parkside</p>
  <p class="contact" style="top:4618px"><svg viewBox="0 0 14 14"><path d="M3 1h3l1 3-2 1a8 8 0 0 0 4 4l1-2 3 1v3c0 1-1 2-2 2A11 11 0 0 1 1 3c0-1 1-2 2-2z" fill="#555"/></svg>+10042217</p>
  <p class="contact" style="top:4660px"><svg viewBox="0 0 14 14"><rect x="1" y="3" width="12" height="8" fill="none" stroke="#555" stroke-width="1.3"/><path d="M1 3l6 5 6-5" fill="none" stroke="#555" stroke-width="1.3"/></svg>hello@kinoramed.com</p>
  <div class="foot-col" style="left:482px">
    <span class="bar"></span><h4>Quick Links</h4>
    <ul><li>Home</li><li>About Us</li><li>Solutions</li><li>Testimonials</li><li>Appointment</li><li>Contact</li><li>24/7 Support</li></ul>
  </div>
  <div class="foot-col" style="left:792px">
    <span class="bar"></span><h4>Opening Hours</h4>
    <ul><li>Mon - Tue: 9.00 - 17.00</li><li>Wed - Thur: 9.00 - 16.00</li><li>Fri - Sat: 9.00 - 12.00</li><li>Saturday: 9.00 - 14.00</li><li class="closed">Sunday: Closed</li></ul>
  </div>
  <div class="copy">Copyright @ 2020 www.kinoramed.com . All Rights Reserved</div>
</footer>

</body>
</html>
```